Tildens Biscuit Barn Website

I need a website for a diner/restaurant that has been established in a farming, oil and industrial community for over 15 years. The website needs to be simple in design, but that should demonstrate the mastery of skills of the designer. Our diner/restaurant is family oriented, patriotic but very rustic
Fb Address is fb.me/TildensBarn

Pictures of the restaurant

https://www.filecrate-example.net/s/qk72hdw01/Tildens_05.jpg

Pictures of About us

https://www.filecrate-example.net/sh/zm40vrt88/AboutUsPhotos

Article about Tilden's
https://www.filecrate-example.net/s/wp31nbx57/TildensBiscuitBarn1.PDF
https://www.filecrate-example.net/s/hy65lcu29/TildensBiscuitBarn2.PDF

Reason: I was slow to update with information.

Reason: I am just getting feedback to the designs posted. I wasn't sure of the limited feedback was limiting designers from submitting designs. That and running a business with 25 employees open 12 hours a day, being here 2 hours prior and 2-3 hours after makes for long days.

I've increased the first place prize and also added funds to the second and third place prizes for your effort.

I just need the files in PSD, not HTML 5 as originally requested. We can handle getting the coding part.

Ill have the contest finalized by Monday. Thanks for your patience.

Target Market(s)

Cross section of adults from 18-35 & 35-55.

Industry/Entity Type

Industrial

Font styles to use
Other font styles liked:
• ff tisa web pro or garamond premier pro

Requirements
Must have
• Must be clean, look nice and not look like an afterthought.
Nice to have
• Please see the last two documents for information about our restaurant, which was featured in our local newspaper.

```html
<!DOCTYPE html>
<html lang="en">
<head>
<meta charset="utf-8">
<title>Tildens Biscuit Barn – Welcome</title>
<link rel="stylesheet" href="https://fonts.googleapis.com/css2?family=EB+Garamond:wght@400;500&family=Yellowtail&family=Playball&display=swap">
<style>
  :root {
    --wood-light: #f1f1f0;
    --wood-mid: #e2e3e4;
    --plank-line: #c9cbce;
    --brand-red: #a8173a;
    --ink: #1f1c1a;
    --band-black: #0b0b0b;
    --band-glow: #2c2c2c;
    --trim-gold: #e0ac62;
    --paper: #efefed;
    --paper-edge: #dcdcd9;
    --chalk: #e9e9e9;
    --logo-blue: #2c5d78;
  }
  * { margin: 0; padding: 0; box-sizing: border-box; }
  html, body { width: 1068px; height: 1200px; overflow: hidden; }
  body {
    position: relative;
    background: linear-gradient(180deg, var(--wood-light) 0%, var(--wood-mid) 50%, var(--wood-light) 100%);
    font-family: "EB Garamond", Georgia, serif;
    color: var(--ink);
  }
  .wood-backdrop {
    position: absolute; inset: 0;
    background: linear-gradient(90deg, #ebebeb, #f4f4f4 40%, #e6e7e8);
  }
  .site-header { position: absolute; left: 0; top: 0; width: 1068px; height: 233px; }
  .brand {
    position: absolute; left: 52px; top: 70px;
    display: flex; align-items: center; gap: 8px;
  }
  .brand-dot { width: 14px; height: 14px; border-radius: 50%; background: var(--logo-blue); }
  .brand-name {
    font-family: "EB Garamond", Georgia, serif;
    font-weight: 500; font-size: 34px; color: var(--brand-red); line-height: 1;
  }
  .welcome-title {
    position: absolute; left: 350px; top: 20px; width: 560px;
    text-align: center;
    font-family: "Yellowtail", cursive;
    font-weight: 400; font-size: 138px; line-height: 1;
    color: var(--brand-red);
  }
  .main-nav {
    position: absolute; left: 0; top: 233px; width: 1068px; height: 221px;
    border-top: 7px solid var(--trim-gold);
    border-bottom: 11px solid var(--trim-gold);
    background: radial-gradient(ellipse at 55% 40%, var(--band-glow) 0%, var(--band-black) 70%);
  }
  .nav-item {
    position: absolute; top: 20px; width: 200px; margin-left: -100px;
    display: flex; flex-direction: column; align-items: center;
    color: var(--chalk); text-decoration: none;
  }
  .nav-item svg, .nav-item .founder-portrait { width: 120px; height: 120px; }
  .founder-portrait {
    display: block; border-radius: 50% 50% 42% 42%;
    background: radial-gradient(circle at 50% 45%, #d9d9d9 0%, #8e8e8e 55%, #2a2a2a 100%);
  }
  .nav-label {
    font-family: "Playball", cursive;
    font-size: 40px; line-height: 1; margin-top: 10px;
  }
  .nav-home { left: 158px; }
  .nav-menu { left: 389px; }
  .nav-news { left: 632px; }
  .nav-founder { left: 879px; }
  .nav-founder .nav-label { font-size: 32px; margin-top: 14px; }

  .content-sheet {
    position: absolute; left: 85px; top: 454px; width: 903px; height: 710px;
    background: linear-gradient(180deg, var(--paper) 0%, #f3f3f1 50%, var(--paper-edge) 100%);
    box-shadow: 0 2px 4px rgba(0,0,0,0.12);
  }
  .intro {
    position: absolute; left: 49px; top: 66px; width: 808px;
    font-size: 27px; line-height: 35px;
    text-align: justify; text-align-last: center;
  }
  .find-us-title {
    position: absolute; left: 0; top: 222px; width: 903px;
    text-align: center;
    font-family: "Yellowtail", cursive;
    font-size: 74px; line-height: 1; color: var(--brand-red);
  }
  .hours { position: absolute; top: 386px; left: 0; width: 903px; font-size: 35px; line-height: 1; }
  .hours span { position: absolute; white-space: nowrap; transform: translateX(-50%); }
  .hours .days { left: 215px; }
  .hours .sep { left: 440px; }
  .hours .time { left: 680px; }
  .address {
    position: absolute; left: 0; top: 488px; width: 903px;
    text-align: center; font-size: 35px; line-height: 44px;
  }
  .payment {
    position: absolute; left: 0; top: 598px; width: 903px;
    text-align: center; font-size: 27px; line-height: 35px;
  }
</style>
</head>
<body>
  <div class="wood-backdrop" role="img" aria-label="Whitewashed wooden plank wall"></div>

  <header class="site-header">
    <div class="brand">
      <span class="brand-dot"></span>
      <span class="brand-name">Tilden's</span>
    </div>
    <h1 class="welcome-title">Welcome</h1>
  </header>

  <nav class="main-nav">
    <a class="nav-item nav-home" href="#home">
      <svg viewBox="0 0 120 120" aria-hidden="true">
        <path d="M60 8 L114 58 L100 58 L100 112 L20 112 L20 58 L6 58 Z" fill="#e6e6e6"/>
        <rect x="48" y="84" width="24" height="28" fill="#0b0b0b"/>
      </svg>
      <span class="nav-label">Home</span>
    </a>
    <a class="nav-item nav-menu" href="#menu">
      <svg viewBox="0 0 120 120" aria-hidden="true">
        <g stroke="#e6e6e6" stroke-width="10" stroke-linecap="round">
          <line x1="30" y1="36" x2="98" y2="112"/>
          <line x1="88" y1="46" x2="22" y2="112"/>
        </g>
        <ellipse cx="98" cy="28" rx="18" ry="24" transform="rotate(40 98 28)" fill="#e6e6e6"/>
        <g stroke="#e6e6e6" stroke-width="6" stroke-linecap="round">
          <line x1="8" y1="26" x2="26" y2="8"/>
          <line x1="14" y1="32" x2="32" y2="14"/>
          <line x1="20" y1="38" x2="38" y2="20"/>
        </g>
      </svg>
      <span class="nav-label">Menu</span>
    </a>
    <a class="nav-item nav-news" href="#news">
      <svg viewBox="0 0 120 120" aria-hidden="true">
        <rect x="12" y="6" width="96" height="106" fill="#e6e6e6"/>
        <rect x="20" y="14" width="80" height="10" fill="#5a5a5a"/>
        <rect x="66" y="30" width="34" height="74" fill="#9a9a9a"/>
        <g stroke="#4a4a4a" stroke-width="4">
          <line x1="20" y1="36" x2="58" y2="36"/><line x1="20" y1="46" x2="58" y2="46"/>
          <line x1="20" y1="56" x2="58" y2="56"/><line x1="20" y1="66" x2="58" y2="66"/>
          <line x1="20" y1="76" x2="58" y2="76"/><line x1="20" y1="86" x2="58" y2="86"/>
          <line x1="20" y1="96" x2="58" y2="96"/>
        </g>
      </svg>
      <span class="nav-label">News</span>
    </a>
    <a class="nav-item nav-founder" href="#founder">
      <span class="founder-portrait" role="img" aria-label="Chalk-style portrait of the founder in a hard hat"></span>
      <span class="nav-label">Our founder</span>
    </a>
  </nav>

  <main class="content-sheet">
    <p class="intro">Text about the coffee shop, its qualities, etc. Lorem ipsum dolor sit amet, consectetur adipiscing elit. Nunc vestibulum ipsum condimentum mauris porta efficitur. Morbi ut lorem sed elit interdum convallis.</p>

    <h2 class="find-us-title">Find Us</h2>

    <p class="hours">
      <span class="days">Monday to Sunday</span>
      <span class="sep">•</span>
      <span class="time">5:30 AM to 2:00 PM</span>
    </p>

    <p class="address">4810 Harrow Field Road<br>555-0147</p>

    <p class="payment">NorthCard, Velacard, Ameridon Express,<br>Farpoint and personal checks accepted.</p>
  </main>
</body>
</html>
```